Design/Build Engineering and Detailing Service 3D Modeling

We are an engineering company in the construction industry. We specialize in designing blueprints for new construction projects such as high rise buildings, hospitals, hotels, public schools, large scale apartment buildings etc.

We want to have a clean, modern, cutting edge design, but it should be clear and easy to navigate. Related videos in the background of the page are a plus. For example The page now has a picture of the harlow creek bridge in san francisco with fog rolling over it and cars driving on the bridge, saying website coming soon. This is played at a faster frame rate. We want to have customer portal to access files, fill out work orders, pay invoices, make suggestions etc.
Updates

Target Market(s)

Los Angeles, San francisco, San Jose, Portland, Seattle, Las Vegas, Denver

Industry/Entity Type

Construction

Coding

Coded - Design and coding required

Number of Pages Required

4 page

Font styles to use
Serif
Sans Serif

Colors
3276b5
0255a3
85acd3
9d9d9d
5c5c5c
ec1f27
000000
fbee3f
00a990

Requirements
Must have
• Work Examples, mission statement, team members, capabilities. Convey the technical aspects of the business in a way that someone can understand the companies capabilities without knowing the technical side of the business.
Nice to have
• Construction related Videos, Downtown city center skylines, clean, modern, concise design.
Should not have
• Overly complex navigation. should not be to busy

```html
<!DOCTYPE html>
<html lang="en">
<head>
<meta charset="utf-8">
<title>Corbel Designs Inc — 3D BIM Design/Build</title>
<link href="https://fonts.googleapis.com/css2?family=Roboto:wght@400;500;700&family=Roboto+Condensed:wght@400;700&family=Open+Sans:ital,wght@0,400;0,600;1,400&display=swap" rel="stylesheet">
<style>
  :root{
    --brand:#1f5aa6;
    --brand-dark:#0d4597;
    --band:#0f4da0;
    --accent:#f15a22;
    --ink:#222;
    --muted:#555;
    --soft:#9d9d9d;
    --line:#e2e2e2;
    --footer:#efefef;
    --white:#fff;
  }
  *{box-sizing:border-box;margin:0;padding:0}
  html,body{width:1200px;height:2586px;overflow:hidden;background:var(--white)}
  body{position:relative;font-family:"Open Sans",sans-serif;color:var(--ink)}
  .abs{position:absolute}
  h1,h2,h3,h4,.nav a,.btn{font-family:"Roboto",sans-serif}

  /* header */
  .site-header{position:absolute;left:0;top:0;width:1200px;height:98px;background:var(--white);box-shadow:0 2px 6px rgba(0,0,0,.12);z-index:2}
  .brand{position:absolute;left:98px;top:30px;display:flex;align-items:center;gap:12px}
  .brand-mark{width:34px;height:34px;background:var(--brand)}
  .brand-name{font-family:"Roboto Condensed",sans-serif;font-weight:700;font-size:32px;color:var(--brand);letter-spacing:.3px}
  .nav a{position:absolute;top:0;height:98px;line-height:98px;font-size:13px;font-weight:500;color:#222;text-decoration:none;text-transform:uppercase}
  .nav a.active{background:var(--brand);color:var(--white);width:82px;text-align:center}

  /* hero */
  .hero{position:absolute;left:0;top:98px;width:1200px;height:522px;
    background:
      radial-gradient(ellipse 420px 160px at 560px 400px,rgba(190,110,70,.35),rgba(190,110,70,0) 70%),
      radial-gradient(ellipse 260px 300px at 980px 220px,rgba(120,150,170,.35),rgba(120,150,170,0) 70%),
      linear-gradient(180deg,#6b737b 0%,#4c5660 30%,#2f3841 62%,#1b2128 100%)}
  .hero-title{position:absolute;left:0;width:1200px;text-align:center;color:var(--white);font-family:"Roboto Condensed",sans-serif;font-weight:700;text-shadow:0 2px 4px rgba(0,0,0,.4)}
  .hero-title.l1{top:216px;font-size:50px}
  .hero-title.l2{top:270px;font-size:38px}
  .hero-arrow{position:absolute;top:245px;width:32px;height:32px;border-radius:50%;background:rgba(0,0,0,.45)}

  /* about */
  .about-visual{left:107px;top:683px;width:472px;height:331px;
    background:radial-gradient(ellipse 260px 190px at 50% 50%,#3a72c8,#1c4ea3 60%,#0f357c)}
  .about-copy{position:absolute;left:624px;top:686px;width:462px}
  .about-copy h2{font-size:30px;font-weight:400;color:#222;line-height:36px}
  .about-copy h3{margin-top:9px;font-size:18px;font-weight:400;color:#222;line-height:24px}
  .about-copy p{margin-top:12px;font-size:11.8px;line-height:20.5px;color:var(--muted)}
  .about-copy p + p{margin-top:14px}
  .about-copy .btn{margin-top:24px;width:130px;height:35px;line-height:35px}
  .btn{display:block;text-align:center;color:var(--white);background:var(--accent);font-size:14px;font-weight:500;text-transform:uppercase;border-radius:3px;text-decoration:none}

  /* projects */
  .projects{position:absolute;left:0;top:1083px;width:1200px;height:557px;background:linear-gradient(180deg,#0f4da0,#124c98 70%,#1a4f92)}
  .projects h2{position:absolute;left:0;top:46px;width:1200px;text-align:center;color:var(--white);font-weight:400;font-size:29px}
  .circle-arrow{position:absolute;top:54px;width:28px;height:28px}
  .card{position:absolute;top:117px;width:235px;color:var(--white);text-align:center}
  .card .photo{width:235px;height:188px;border:2px solid var(--white)}
  .card h4{margin-top:16px;font-weight:400;font-size:19px;text-transform:uppercase;white-space:nowrap}
  .card p{margin-top:9px;font-size:11.2px;line-height:19px;letter-spacing:-.1px}

  /* lower */
  .col-title{position:absolute;top:1702px;font-family:"Roboto",sans-serif;font-size:21px;font-weight:400;color:#222;text-transform:uppercase;padding-bottom:12px;border-bottom:1px solid var(--line)}
  .avatar{left:198px;top:1762px;width:114px;height:114px;border-radius:50%;border:3px solid #eee;background:linear-gradient(180deg,#dfe5ec,#8fa0b4)}
  .person{left:98px;top:1884px;width:314px;text-align:center;font-size:16px;color:#333}
  .quote{left:104px;top:1913px;width:310px;font-style:italic;font-size:11.2px;line-height:19.5px;color:#333;text-align:center}
  .event-img{left:452px;width:98px;height:93px}
  .event{left:569px;width:200px}
  .event h4{font-weight:400;font-size:15.5px;color:#222;white-space:nowrap}
  .event .date{margin-top:6px;font-size:12px;color:var(--accent)}
  .event p{margin-top:6px;font-size:11.2px;line-height:18px;color:#444}
  .promo{left:796px;top:1707px;width:302px;height:289px;background:linear-gradient(180deg,#7a8fd0 0%,#5b7cc0 40%,#4e6f9e 70%,#5c6b78 100%)}
  .promo span{position:absolute;left:0;top:14px;width:302px;text-align:center;color:var(--white);font-family:"Roboto Condensed",sans-serif;font-weight:700;font-size:15px;line-height:22px;text-transform:uppercase}

  .divider{left:300px;top:2052px;width:600px;height:1px;background:var(--line);box-shadow:0 -8px 16px rgba(0,0,0,.06)}
  .awards-title{left:0;top:2081px;width:1200px;text-align:center;font-size:25px;font-weight:400;color:#222}
  .award{position:absolute;top:2143px;width:156px;height:78px;border:1px solid var(--line)}
  .award i{position:absolute;left:58px;top:19px;width:40px;height:40px;border-radius:50%;background:#c9c9c9}

  /* footer */
  .footer{position:absolute;left:0;top:2262px;width:1200px;height:278px;background:var(--footer)}
  .footer h4{position:absolute;top:46px;font-weight:400;font-size:16px;color:#222;text-transform:uppercase}
  .info-list{position:absolute;left:98px;top:94px;list-style:none;font-size:12px;line-height:23px;color:#333}
  .map{position:absolute;left:272px;top:86px;width:266px;height:150px;background:linear-gradient(135deg,#e4e2da,#d3d9cc 60%,#c9d3de);border:1px solid #ddd}
  .news-text{position:absolute;left:610px;top:94px;width:240px;font-size:11.5px;line-height:20px;color:#444}
  .input{position:absolute;left:610px;top:131px;width:243px;height:43px;background:var(--white);border:1px solid #ddd;font-size:12px;line-height:41px;padding-left:14px;color:#444}
  .subscribe{position:absolute;left:610px;top:186px;width:102px;height:42px;line-height:42px;background:var(--brand);border-radius:0;font-size:13px}
  .f-brand{position:absolute;left:914px;top:64px;font-family:"Roboto Condensed",sans-serif;font-weight:700;font-size:26px;color:var(--brand)}
  .contact{position:absolute;left:924px;font-size:13px;line-height:20px;color:#333;display:flex;gap:14px;align-items:flex-start}
  .contact svg{flex:none;margin-top:2px}
  .bottom-bar{position:absolute;left:0;top:2540px;width:1200px;height:46px;background:var(--brand-dark);color:var(--white);font-size:12px}
  .bottom-bar .copy{position:absolute;left:107px;top:15px}
  .bottom-bar .legal{position:absolute;left:914px;top:15px}
</style>
</head>
<body>

<header class="site-header">
  <div class="brand"><span class="brand-mark"></span><span class="brand-name">CORBEL DESIGNS INC</span></div>
  <nav class="nav">
    <a class="active" href="#" style="left:490px">Home</a>
    <a href="#" style="left:598px">About Us</a>
    <a href="#" style="left:705px">Our Services</a>
    <a href="#" style="left:831px">Projects</a>
    <a href="#" style="left:936px">Awards</a>
    <a href="#" style="left:1034px">Contact Us</a>
  </nav>
</header>

<section class="hero" role="img" aria-label="Dusk view of a modern glass and steel commercial building">
  <span class="hero-arrow" style="left:32px"></span>
  <span class="hero-arrow" style="left:1130px"></span>
  <svg class="abs" style="left:32px;top:245px" width="32" height="32"><path d="M19 10l-6 6 6 6" stroke="#fff" stroke-width="2" fill="none"/></svg>
  <svg class="abs" style="left:1130px;top:245px" width="32" height="32"><path d="M13 10l6 6-6 6" stroke="#fff" stroke-width="2" fill="none"/></svg>
  <h1 class="hero-title l1">3D BIM DESIGN/BUILD</h1>
  <div class="hero-title l2">COMMERCIAL</div>
</section>

<section class="about">
  <div class="abs about-visual" role="img" aria-label="Blueprint wireframe drawing of a house"></div>
  <div class="about-copy">
    <h2>ABOUT OUR COMPANY</h2>
    <h3>We are currently working for Orchard in building their new office</h3>
    <p>16 years experience in new commercial/ industrial construction specializing in plumbing and hydronic piping systems. Elias's responsibilities are to manage department personnel, coordinate BIM efforts, QA/QC, detailing, shop drawings, piping design (domestic water and sanitary waste), mechanical system design (heating hot water and chilled water) and spooling for traditional and IPD projects.</p>
    <p>These responsibilities all culminate into delivering a constructible, efficient, and cost effective design that distributes savings to the owner over the life span of the building, campus, or facility.</p>
    <a class="btn" href="#">Read More
      <svg width="13" height="13" style="vertical-align:-2px"><circle cx="6.5" cy="6.5" r="6.5" fill="#fff"/><path d="M5 3.5l3 3-3 3" stroke="#f15a22" stroke-width="1.6" fill="none"/></svg></a>
  </div>
</section>

<section class="projects">
  <svg class="circle-arrow" style="left:100px" viewBox="0 0 28 28"><circle cx="14" cy="14" r="13" stroke="#fff" stroke-width="1.5" fill="none"/><path d="M16 9l-5 5 5 5" stroke="#fff" stroke-width="1.5" fill="none"/></svg>
  <svg class="circle-arrow" style="left:1072px" viewBox="0 0 28 28"><circle cx="14" cy="14" r="13" stroke="#fff" stroke-width="1.5" fill="none"/><path d="M12 9l5 5-5 5" stroke="#fff" stroke-width="1.5" fill="none"/></svg>
  <h2>PROJECTS WORK</h2>

  <article class="card" style="left:100px">
    <div class="photo" role="img" aria-label="Modern office building with glass facade" style="background:linear-gradient(180deg,#2f78c4 0%,#6fa0c8 35%,#a9b4b8 60%,#5c8e48 100%)"></div>
    <h4>Orchard Campus 2</h4>
    <p>Orchard campus 2 is a four story, 2.8 million square foot building in Ridgemont, Ca. Elias is responsible for the water</p>
  </article>
  <article class="card" style="left:355px">
    <div class="photo" role="img" aria-label="Hospital emergency entrance building" style="background:linear-gradient(180deg,#8fb3d6 0%,#b5795a 30%,#c9c2b6 55%,#6d6a66 100%)"></div>
    <h4>The Meridian Center</h4>
    <p>The Meridian Center for the Performing Arts is in Downtown Las Vegas's 61-acre Civic Park and is a five-acre,</p>
  </article>
  <article class="card" style="left:612px">
    <div class="photo" role="img" aria-label="Ornate hotel lobby interior" style="background:linear-gradient(180deg,#4a2616 0%,#a8743e 40%,#c99a5a 60%,#3c2216 100%)"></div>
    <h4>Crescent Plaza</h4>
    <p>Crescent Plaza is a 9 billion dollar gaming and hospitality project at the center of the Las Vegas strip.</p>
  </article>
  <article class="card" style="left:865px">
    <div class="photo" role="img" aria-label="Brick school building with green lawn" style="background:linear-gradient(180deg,#a9cbe8 0%,#3f7d3a 25%,#9a6e4e 50%,#5aa83e 80%,#4f9a3a 100%)"></div>
    <h4>Northfield Career</h4>
    <p>Northfield Career &amp; Tech is part of the Harlan County School District and a Lumen Apps for Education site.</p>
  </article>

  <a class="btn abs" href="#" style="left:519px;top:469px;width:164px;height:41px;line-height:41px">View Portfolio</a>
</section>

<section class="lower">
  <h3 class="col-title" style="left:98px;width:314px">Testimonials</h3>
  <div class="abs avatar" role="img" aria-label="Portrait of a client"></div>
  <div class="abs person">Mark Ellison</div>
  <p class="abs quote">“ Elias is a meticulous to detail &amp; very conscience of budgets and timetables. Nam libero tempore, cum soluta nobis est eligendi optio cumque nihil impedit quo minus id quod maxime placeat facere possimus, omnis</p>

  <h3 class="col-title" style="left:452px;width:312px">Latest Events</h3>
  <div class="abs event-img" style="top:1772px;background:linear-gradient(135deg,#c8d7e6,#b58a6a)" role="img" aria-label="Family in front of a new home"></div>
  <div class="abs event" style="top:1770px">
    <h4>New commercial/ industrial</h4>
    <div class="date">Aug 20, 2016</div>
    <p>Corbel Designs Incorporated is a full service Detailing firm that specializes in complete plumbing</p>
  </div>
  <div class="abs event-img" style="top:1894px;background:linear-gradient(135deg,#d6e2ee,#9c8a7a)" role="img" aria-label="Couple in front of a house"></div>
  <div class="abs event" style="top:1892px">
    <h4>New commercial/ industrial</h4>
    <div class="date">Aug 20, 2016</div>
    <p>Corbel Designs Incorporated is a full service Detailing firm that specializes in complete plumbing</p>
  </div>

  <div class="abs promo" role="img" aria-label="Modern multi-storey office building under blue sky">
    <span>We are currently working<br>for Orchard in building their<br>new office</span>
  </div>

  <div class="abs divider"></div>
  <h2 class="abs awards-title">OUR AWARDS</h2>
  <div class="award" style="left:257px"><i></i></div>
  <div class="award" style="left:436px"><i></i></div>
  <div class="award" style="left:615px"><i></i></div>
  <div class="award" style="left:788px"><i></i></div>
</section>

<footer class="footer">
  <h4 style="left:98px">Information</h4>
  <ul class="info-list">
    <li>High Rise Buildings</li>
    <li>Hospitals, Hotels</li>
    <li>Public Schools</li>
    <li>Large Scale Apartment</li>
    <li>Buildings</li>
  </ul>

  <h4 style="left:271px">Our Location</h4>
  <div class="map" role="img" aria-label="Street map of the office location"></div>

  <h4 style="left:610px">Join Our Newsletter</h4>
  <p class="news-text">Excepteur sint occaecat cupidatat non proident, sunt in culpa qui</p>
  <div class="input">Enter Name</div>
  <a class="btn subscribe" href="#">Subscribe</a>

  <div class="f-brand">CORBEL DESIGNS INC</div>
  <div class="contact" style="top:119px">
    <svg width="16" height="22" viewBox="0 0 16 22"><path d="M8 1a7 7 0 0 0-7 7c0 5 7 13 7 13s7-8 7-13a7 7 0 0 0-7-7z" fill="none" stroke="#1f5aa6" stroke-width="1.5"/><circle cx="8" cy="8" r="2.5" fill="none" stroke="#1f5aa6" stroke-width="1.5"/></svg>
    <span>Corbel Designs Inc<br>PO BOX TBA, Westbrook</span>
  </div>
  <div class="contact" style="top:167px">
    <svg width="16" height="16" viewBox="0 0 16 16"><path d="M3 1l3 3-2 2c1 2 3 4 5 5l2-2 3 3-2 3C7 15 1 9 1 3z" fill="none" stroke="#1f5aa6" stroke-width="1.4"/></svg>
    <span>+1 0400 555 018</span>
  </div>
  <div class="contact" style="top:193px">
    <svg width="16" height="14" viewBox="0 0 16 14"><rect x="1" y="1" width="14" height="12" fill="none" stroke="#1f5aa6" stroke-width="1.4"/><path d="M1 1l7 6 7-6" fill="none" stroke="#1f5aa6" stroke-width="1.4"/></svg>
    <span>info@corbeldesigns.com</span>
  </div>
</footer>

<div class="bottom-bar">
  <span class="copy">©2016 Corbel Designs Inc. All Rights Reserved.</span>
  <span class="legal">Privacy Policy &nbsp;/&nbsp; Terms &amp; Conditions</span>
</div>

</body>
</html>
```